wedding DJ & Lighting entertainment

We are a DJ and Lighting production company. We specialize mainly in wedding entertainment. I've attached my old postcard in the image folder, however, i would like something new and updated. You can use the same bullet points from the front page, but i would like to have a cleaner look on the front. I'd like to have one large image on the front side and smaller images on the back side. I'd also like to have some text below the logo. I'd like it to say DJ * Lighting * Audio/Visual. I'd also like to have the phrase "Celebrate with Style"

Target Market(s)

weddings, private events, women

Industry/Entity Type

It Company

Font styles to use
Sans Serif
Script

Requirements
Must have
• look elegant, sophisticated. Must have my new logo! My logo is attached as one of the files. It's a headphone logo.

```html
<!DOCTYPE html>
<html lang="en">
<head>
<meta charset="utf-8">
<title>Brightnote Events – Postcard Front and Back</title>
<link rel="stylesheet" href="https://fonts.googleapis.com/css2?family=Great+Vibes&family=Cinzel:wght@400&family=Questrial&display=swap">
<style>
  :root {
    --bg: #6e6e6e;
    --ink-white: #ffffff;
    --accent-red: #e0262b;
    --dark-band: #120c12;
    --strip-gray: #b9b9b9;
    --photo-warm-1: #5b2a5e;
    --photo-warm-2: #b5553a;
    --photo-warm-3: #2a1830;
    --photo-mono-1: #2b2b2b;
    --photo-mono-2: #7a7a7a;
  }
  * { margin: 0; padding: 0; box-sizing: border-box; }
  html, body { width: 1200px; height: 573px; overflow: hidden; }
  body { background: var(--bg); position: relative; font-family: "Questrial", sans-serif; }

  .card { position: absolute; top: 64px; height: 406px; overflow: hidden; }
  .card--front { left: 54px; width: 526px; }
  .card--back { left: 614px; width: 530px; }

  .photo { position: absolute; inset: 0; }
  .photo--front-main {
    background:
      radial-gradient(ellipse at 60% 20%, #c04ab0 0%, transparent 45%),
      radial-gradient(ellipse at 45% 70%, var(--photo-warm-2) 0%, transparent 55%),
      linear-gradient(180deg, var(--photo-warm-1) 0%, #7a3a48 55%, var(--photo-warm-3) 100%);
  }
  .photo--back-main {
    background:
      radial-gradient(ellipse at 30% 30%, #9a9a9a 0%, transparent 50%),
      radial-gradient(ellipse at 80% 80%, #8a8a8a 0%, transparent 45%),
      linear-gradient(180deg, #1a1a1a 0%, var(--photo-mono-1) 40%, var(--photo-mono-2) 100%);
  }

  .brand { position: absolute; display: flex; align-items: center; gap: 6px; color: var(--ink-white); }
  .brand__dot { width: 10px; height: 10px; border-radius: 50%; background: var(--accent-red); }
  .brand__name { font-family: "Questrial", sans-serif; font-size: 19px; letter-spacing: 0.5px; }
  .brand-block { position: absolute; text-align: center; color: var(--ink-white); }
  .brand-block__url { font-size: 8.5px; margin-top: 4px; letter-spacing: 0.3px; }

  .front-brand { left: 20px; top: 60px; width: 150px; }
  .front-brand .brand { position: static; justify-content: center; }

  .tagline-script {
    position: absolute; left: 200px; top: 48px; width: 290px; text-align: center;
    font-family: "Great Vibes", cursive; font-size: 30px; color: var(--ink-white);
    text-shadow: 0 1px 4px rgba(0,0,0,0.6);
  }

  .services-band {
    position: absolute; left: 0; right: 0; bottom: 0; height: 110px;
    background: linear-gradient(180deg, rgba(18,12,18,0) 0%, var(--dark-band) 35%);
  }
  .services-title {
    position: absolute; left: 0; right: 0; top: 308px; text-align: center;
    font-family: "Cinzel", serif; font-size: 28px; color: var(--ink-white); letter-spacing: 0.5px;
  }
  .services-list {
    position: absolute; left: 20px; right: 20px; top: 350px; list-style: none;
    display: flex; flex-wrap: wrap; justify-content: center; column-gap: 9px; row-gap: 3px;
    color: var(--ink-white); font-size: 12.5px;
  }
  .services-list li { display: flex; align-items: center; gap: 4px; }
  .services-list li::before {
    content: ""; width: 5px; height: 5px; border-radius: 50%; background: var(--accent-red);
  }

  .tagline-caps {
    position: absolute; left: 0; right: 0; top: 60px; text-align: center;
    font-family: "Cinzel", serif; font-size: 30px; color: var(--accent-red); letter-spacing: 0.5px;
  }
  .gallery-strip {
    position: absolute; left: 0; right: 0; top: 142px; height: 98px;
    background: rgba(200,200,200,0.85);
  }
  .gallery-photo { position: absolute; top: 148px; height: 86px; }
  .gallery-photo--crowd-mono { left: 21px; width: 86px; background: linear-gradient(160deg, #d8d8d8, #3a3a3a); }
  .gallery-photo--first-dance { left: 113px; width: 182px; background: radial-gradient(ellipse at 55% 60%, #d9c98a 0%, #4b2b6e 45%, #231433 100%); }
  .gallery-photo--crowd-pink { left: 302px; width: 91px; background: linear-gradient(180deg, #e4469e 0%, #8a3a6e 55%, #3a2030 100%); }
  .gallery-photo--lit-room { left: 399px; width: 110px; background: linear-gradient(180deg, #7aa0d8 0%, #6a4ab0 50%, #2c2450 100%); }

  .back-brand { left: 190px; top: 318px; width: 150px; }
  .back-brand .brand { position: static; justify-content: center; }
  .back-contact { font-size: 9.5px; margin-top: 8px; }
  .back-phone { font-size: 14px; margin-top: 3px; letter-spacing: 0.5px; }
</style>
</head>
<body>
  <section class="card card--front">
    <div class="photo photo--front-main" role="img" aria-label="Wedding guests dancing in a circle around the bride under purple and pink uplighting"></div>
    <div class="brand-block front-brand">
      <div class="brand"><span class="brand__dot"></span><span class="brand__name">Brightnote Events</span></div>
      <div class="brand-block__url">www.brightnoteevents.com</div>
    </div>
    <p class="tagline-script">“Celebrate with Style”</p>
    <div class="services-band"></div>
    <h2 class="services-title">DJ * LIGHTING * AUDIO/VISUAL</h2>
    <ul class="services-list">
      <li>DJ &amp; Emcee Entertainment</li>
      <li>Customized Lighting Décor</li>
      <li>Helpful Planning tools</li>
      <li>Event Hosting &amp; Coordination</li>
      <li>Personalized Service</li>
    </ul>
  </section>

  <section class="card card--back">
    <div class="photo photo--back-main" role="img" aria-label="Black and white photo of party guests cheering with raised arms"></div>
    <h2 class="tagline-caps">“CELEBRATE WITH STYLE”</h2>
    <div class="gallery-strip"></div>
    <div class="gallery-photo gallery-photo--crowd-mono" role="img" aria-label="Guests with hands raised on the dance floor"></div>
    <div class="gallery-photo gallery-photo--first-dance" role="img" aria-label="Couple sharing a first dance in a purple-lit ballroom"></div>
    <div class="gallery-photo gallery-photo--crowd-pink" role="img" aria-label="Crowd dancing under pink lights"></div>
    <div class="gallery-photo gallery-photo--lit-room" role="img" aria-label="Reception room with blue and purple uplighting and monogram on the floor"></div>
    <div class="brand-block back-brand">
      <div class="brand"><span class="brand__dot"></span><span class="brand__name">Brightnote Events</span></div>
      <div class="back-contact">www.brightnoteevents.com</div>
      <div class="back-phone">555-014-2087</div>
    </div>
  </section>
</body>
</html>
```